Field Mentors UK award course Flyer Design

Flyer design required for a social enterprise called "Bright Arena" - logo attached - to promote our Field Mentors Award course(s).

The course is targeted at individuals aged 13+ and will develop leadership skills that transfer beyond the sporting environment. It is a fun and practical course that focusses on leading rather than sporting ability or technical knowledge and leads on to further qualifications or awards. Individuals' self-confidence will improve and the course is a potential stepping stone in to employment, further education or training.

The course will be run at Quarrybank Community Sports Centre, Ashcombe School, Tollard Lane, Wrenford. ZX4 7QP. On Monday 20th July to Friday 24th July.
There is a subsidised fee of £15

We are a Regional Academy for Field Mentors UK.

The company's main colour is royal blue but please make the design as attractive and eye-catching to young people, male and female, as possible.

```html
<!DOCTYPE html>
<html lang="en">
<head>
<meta charset="utf-8">
<title>Field Mentors Award – Bright Arena Flyer</title>
<link href="https://fonts.googleapis.com/css2?family=Anton&family=Roboto:wght@400;700&display=swap" rel="stylesheet">
<style>
  :root {
    --navy: #14285a;
    --royal: #1f3f8f;
    --red: #e3171d;
    --yellow: #ffe11a;
    --yellow-edge: #e0a800;
    --sky-top: #b9d3e6;
    --sky-bottom: #eef3f6;
    --ink: #1d2a55;
    --page: #e9e9ec;
    --white: #ffffff;
  }
  html, body {
    margin: 0;
    width: 1200px;
    height: 972px;
    overflow: hidden;
    background: var(--page);
  }
  .flyer {
    position: absolute;
    left: 100px;
    top: 86px;
    width: 1000px;
    height: 800px;
    background: var(--white);
    overflow: hidden;
    box-shadow: 0 6px 24px rgba(0,0,0,.18);
    font-family: "Roboto", Arial, sans-serif;
  }
  .hero-photo {
    position: absolute;
    left: 360px;
    top: 0;
    width: 640px;
    height: 640px;
    background: linear-gradient(180deg, var(--sky-top) 0%, var(--sky-bottom) 70%, var(--white) 100%);
  }
  .brand {
    position: absolute;
    right: 60px;
    top: 70px;
    display: flex;
    align-items: center;
    gap: 12px;
  }
  .brand-dot {
    width: 22px;
    height: 22px;
    border-radius: 50%;
    background: var(--navy);
  }
  .brand-name {
    font-family: "Anton", Impact, sans-serif;
    font-size: 40px;
    line-height: 1;
    color: var(--navy);
    text-transform: uppercase;
  }
  .headline {
    position: absolute;
    left: 50px;
    top: 250px;
    width: 380px;
    margin: 0;
    font-family: "Anton", Impact, sans-serif;
    font-weight: 400;
    font-size: 46px;
    line-height: 1.18;
    text-transform: uppercase;
    color: var(--royal);
  }
  .headline .accent { color: var(--red); }
  .enquiries {
    position: absolute;
    right: 40px;
    top: 395px;
    color: var(--ink);
    font-size: 17px;
  }
  .enquiries-title {
    font-family: "Anton", Impact, sans-serif;
    font-size: 21px;
    color: var(--red);
    text-transform: uppercase;
    margin: 0 0 6px;
  }
  .enquiries-line {
    display: flex;
    align-items: center;
    gap: 8px;
    margin: 4px 0;
  }
  .band {
    position: absolute;
    left: 0;
    top: 0;
    width: 1000px;
    height: 800px;
  }
  .fee-badge {
    position: absolute;
    left: 640px;
    top: 505px;
    width: 220px;
    height: 180px;
  }
  .fee-text {
    position: absolute;
    inset: 0;
    display: flex;
    align-items: center;
    justify-content: center;
    text-align: center;
    font-family: "Anton", Impact, sans-serif;
    font-size: 23px;
    line-height: 1.1;
    color: var(--red);
    text-transform: uppercase;
  }
  .details {
    position: absolute;
    left: 30px;
    top: 640px;
    color: var(--white);
    font-size: 22px;
    line-height: 1.25;
  }
  .detail-label {
    display: inline-block;
    background: var(--yellow);
    color: var(--red);
    font-family: "Anton", Impact, sans-serif;
    font-size: 22px;
    padding: 0 8px;
    margin: 4px 0 2px;
    text-transform: uppercase;
  }
  .detail-text { margin: 0; }
</style>
</head>
<body>
  <main class="flyer">
    <div class="hero-photo" role="img" aria-label="Photo of a young child in a superhero mask and red cape, arm raised, against a bright sky"></div>

    <div class="brand"><span class="brand-dot"></span><span class="brand-name">Bright Arena</span></div>

    <h1 class="headline">
      Develop <span class="accent">Leadership</span>
      <span class="accent">Skills</span> that transfer
      beyond the <span class="accent">Sporting</span>
      <span class="accent">Environment.</span>
    </h1>

    <svg class="band" viewBox="0 0 1000 800" aria-hidden="true">
      <polygon points="0,640 1000,470 1000,800 0,800" fill="var(--navy)"/>
    </svg>

    <div class="enquiries">
      <p class="enquiries-title">General Enquiries</p>
      <p class="enquiries-line">
        <svg width="16" height="16" viewBox="0 0 16 16"><circle cx="8" cy="8" r="8" fill="var(--red)"/><path d="M5 4.5l1.6-.4 1 2-1 .8a5 5 0 0 0 2.5 2.5l.8-1 2 1-.4 1.6c-3.6.2-6.7-2.9-6.5-6.5z" fill="var(--white)"/></svg>
        07700 900418
      </p>
      <p class="enquiries-line">
        <svg width="16" height="16" viewBox="0 0 16 16"><circle cx="8" cy="8" r="8" fill="var(--red)"/><rect x="4" y="5" width="8" height="6" fill="none" stroke="var(--white)" stroke-width="1.2"/><path d="M4 5l4 3.3L12 5" fill="none" stroke="var(--white)" stroke-width="1.2"/></svg>
        enquiries@brightarena.org
      </p>
    </div>

    <div class="fee-badge">
      <svg width="220" height="180" viewBox="0 0 220 180" aria-hidden="true">
        <g fill="var(--yellow)" stroke="var(--yellow-edge)" stroke-width="2">
          <circle cx="110" cy="31" r="29"/><circle cx="152" cy="48" r="29"/><circle cx="170" cy="90" r="29"/>
          <circle cx="152" cy="132" r="29"/><circle cx="110" cy="149" r="29"/><circle cx="68" cy="132" r="29"/>
          <circle cx="50" cy="90" r="29"/><circle cx="68" cy="48" r="29"/>
        </g>
        <ellipse cx="110" cy="90" rx="78" ry="62" fill="var(--yellow)"/>
      </svg>
      <div class="fee-text">There is a<br>subsidised<br>fee of £15</div>
    </div>

    <section class="details">
      <span class="detail-label">Venue:</span>
      <p class="detail-text">Quarrybank Community Sports Centre,<br>Ashcombe School, Tollard Lane, Wrenford. ZX4 7QP</p>
      <span class="detail-label">Date &amp; Time:</span>
      <p class="detail-text">On Monday 20th July to Friday 24th July.</p>
    </section>
  </main>
</body>
</html>
```